Life and Personal development life coach needs card design

I need a card design that matches the style and design of my website. I'd like to stay in the same color scheme. Please check out my website for ideas. www.brivelmorcott.com
I have had previous designs for this. I am wondering if you have access to those for more ideas??

```html
<!DOCTYPE html>
<html lang="en">
<head>
<meta charset="utf-8">
<title>Brivel Morcott, RN – Business Card</title>
<link href="https://fonts.googleapis.com/css2?family=Roboto:wght@300;400;700&display=swap" rel="stylesheet">
<style>
  :root {
    --page-bg: #496b12;
    --card-white: #ffffff;
    --leaf: #8cc63f;
    --leaf-deep: #5fa32e;
    --fold-grey: #c4c4c4;
    --fold-grey-light: #d9d9d9;
    --ink-green: #6fb33a;
    --card-shadow: #2f4a08;
  }
  html, body {
    margin: 0;
    padding: 0;
    width: 927px;
    height: 1200px;
    overflow: hidden;
    background: var(--page-bg);
  }
  .sheet {
    width: 927px;
    height: 1200px;
    display: flex;
    flex-direction: column;
    align-items: center;
    justify-content: center;
    gap: 60px;
  }
  .card {
    display: block;
    width: 760px;
    height: 444px;
    box-shadow: 10px 10px 0 var(--card-shadow);
    background: var(--card-white);
  }
  .card text { font-family: "Roboto", Arial, sans-serif; }
  .name { font-weight: 700; font-size: 15px; fill: var(--card-white); }
  .role { font-weight: 400; font-size: 6.2px; fill: var(--card-white); }
  .panel-head { font-weight: 700; font-size: 10px; fill: var(--card-white); }
  .panel-sub { font-weight: 300; font-size: 8.5px; fill: var(--card-white); }
  .values { font-weight: 400; font-size: 7.2px; fill: var(--ink-green); }
  .contact { font-weight: 400; font-size: 8.2px; fill: var(--ink-green); }
  .url { font-weight: 700; font-size: 8px; fill: var(--card-white); letter-spacing: 0.8px; }
  .tagline-strong { font-weight: 700; font-size: 17px; fill: var(--ink-green); }
  .tagline-light { font-weight: 300; font-size: 12.5px; fill: var(--ink-green); letter-spacing: 0.6px; }
</style>
</head>
<body>
<main class="sheet">

  <!-- Front of card -->
  <svg class="card card-front" viewBox="0 0 385 225" aria-label="Front of business card">
    <rect width="385" height="225" fill="var(--card-white)"/>

    <!-- left tagline panel -->
    <rect class="tag-panel" x="0" y="6" width="88" height="72" fill="var(--leaf)"/>
    <text class="panel-head" x="80" y="28" text-anchor="end">Discover</text>
    <text class="panel-head" x="80" y="39" text-anchor="end">what is</text>
    <text class="panel-sub" x="80" y="50" text-anchor="end">possible</text>
    <text class="panel-sub" x="80" y="60" text-anchor="end">today!</text>
    <rect x="0" y="81" width="88" height="4" fill="var(--leaf)"/>
    <g class="ticks" fill="var(--card-white)">
      <rect x="30" y="81" width="1.2" height="4"/>
      <rect x="60" y="81" width="1.2" height="4"/>
    </g>

    <!-- fold -->
    <polygon class="fold-top" points="88,18 123,6 123,66 88,80" fill="var(--leaf-deep)"/>
    <polygon class="fold-face" points="88,86 123,72 123,185 88,200" fill="var(--fold-grey)"/>
    <polygon points="88,86 123,72 123,80 88,94" fill="var(--fold-grey-light)"/>

    <!-- header bar -->
    <rect class="header" x="123" y="6" width="262" height="58" fill="var(--leaf)"/>
    <text class="name" x="137" y="33">BRIVEL MORCOTT, RN</text>
    <text class="role" x="137" y="43">Transformation and Personal Development Life Coach</text>
    <rect x="123" y="66" width="262" height="5" fill="var(--leaf)"/>
    <g class="ticks" fill="var(--card-white)">
      <rect x="160" y="66" width="1.2" height="5"/>
      <rect x="200" y="66" width="1.2" height="5"/>
      <rect x="240" y="66" width="1.2" height="5"/>
      <rect x="280" y="66" width="1.2" height="5"/>
      <rect x="320" y="66" width="1.2" height="5"/>
      <rect x="360" y="66" width="1.2" height="5"/>
    </g>

    <!-- values -->
    <text class="values" x="82" y="155" text-anchor="end">Health,</text>
    <text class="values" x="82" y="164" text-anchor="end">Strength</text>
    <text class="values" x="82" y="173" text-anchor="end">&amp; Balance for</text>
    <text class="values" x="82" y="182" text-anchor="end">Your Mind</text>
    <text class="values" x="82" y="191" text-anchor="end">and Soul</text>

    <!-- contacts -->
    <g class="contacts">
      <text class="contact" x="345" y="103" text-anchor="end">555-014-2290</text>
      <text class="contact" x="345" y="123" text-anchor="end">@brimorc</text>
      <text class="contact" x="345" y="143" text-anchor="end">Brivel Morcott</text>
      <text class="contact" x="345" y="163" text-anchor="end">brivel@brivelmorcott.com</text>

      <rect x="350" y="94" width="32" height="13" fill="var(--leaf-deep)"/>
      <rect x="350" y="114" width="32" height="13" fill="var(--leaf-deep)"/>
      <rect x="350" y="134" width="32" height="13" fill="var(--leaf-deep)"/>
      <rect x="350" y="154" width="32" height="13" fill="var(--leaf-deep)"/>

      <!-- phone icon -->
      <path d="M357 97.5 q2 -1 4 0 l0.6 1.5 h3.8 l0.6 -1.5 q2 -1 4 0 v2 h-2.2 l-0.6 -1 h-7.4 l-0.6 1 h-2.2 z M359 101 h10 v3 h-10 z" fill="var(--card-white)"/>
      <!-- envelope icon -->
      <rect x="357" y="157" width="12" height="8" fill="none" stroke="var(--card-white)" stroke-width="0.9"/>
      <polyline points="357,157 363,162 369,157" fill="none" stroke="var(--card-white)" stroke-width="0.9"/>
    </g>

    <!-- bottom bands -->
    <rect x="0" y="203" width="88" height="9" fill="var(--leaf)"/>
    <polygon points="88,200 123,185 123,195 88,210" fill="var(--leaf-deep)"/>
    <rect x="123" y="185" width="262" height="10" fill="var(--leaf)"/>
    <rect x="0" y="216" width="385" height="3" fill="var(--leaf)"/>
  </svg>

  <!-- Back of card -->
  <svg class="card card-back" viewBox="0 0 385 225" aria-label="Back of business card">
    <rect width="385" height="225" fill="var(--card-white)"/>

    <!-- side bands -->
    <rect x="0" y="55" width="45" height="7" fill="var(--leaf)"/>
    <rect x="340" y="55" width="45" height="7" fill="var(--leaf)"/>
    <polygon points="45,55 63,62 63,72 45,65" fill="var(--leaf-deep)"/>
    <polygon points="340,55 322,62 322,72 340,65" fill="var(--leaf-deep)"/>

    <!-- grey folds -->
    <polygon points="45,65 63,72 63,172 45,160" fill="var(--fold-grey)"/>
    <polygon points="340,65 322,72 322,172 340,160" fill="var(--fold-grey)"/>

    <!-- url band -->
    <rect x="63" y="62" width="259" height="11" fill="var(--leaf)"/>
    <text class="url" x="192.5" y="70.5" text-anchor="middle">www.brivelmorcott.com</text>

    <!-- tagline -->
    <text class="tagline-strong" x="192.5" y="119" text-anchor="middle">Discover what is</text>
    <text class="tagline-light" x="192.5" y="137" text-anchor="middle">possible today!</text>

    <!-- bottom bands -->
    <rect x="0" y="151" width="45" height="9" fill="var(--leaf)"/>
    <rect x="340" y="151" width="45" height="9" fill="var(--leaf)"/>
    <polygon points="45,160 63,165 63,172 45,167" fill="var(--leaf-deep)"/>
    <polygon points="340,160 322,165 322,172 340,167" fill="var(--leaf-deep)"/>
    <rect x="63" y="165" width="259" height="7" fill="var(--leaf)"/>
  </svg>

</main>
</body>
</html>
```